International gaming entertainment company is looking for an innovative Power Point design *

We are looking for a Power Point design for potential international investors, partners and customers in the gaming industry, meaning that a reference to internationality and gaming should become apparent.
The template should be in a reduced and clear style with a combination of innovation and tradition. It should be adaptive and suitable for various applications (tables, shapes and diagrams).
The color scheme of our company are various shades of gray and burgundy (wine-red), however as for the design in question, we are open to other meaningful suggestions (no garish colors).
Updates

Noch kein Design dabei, dass uns 100%ig überzeugt

Target Market(s)

International investors and partners in the gaming industry

Font styles to use
Serif
Sans Serif
Other font styles liked:
• Interstate

Requirements
Must have
• Clear lines
Modern
Footer line with room for classification (eg Confidential, Public) and page number

```html
<!DOCTYPE html>
<html lang="en">
<head>
<meta charset="utf-8">
<title>Vexora Presentation Template Overview</title>
<link href="https://fonts.googleapis.com/css2?family=Oswald:wght@400;500;600&family=Roboto:ital,wght@0,400;0,700;1,400&display=swap" rel="stylesheet">
<style>
:root{
  --red:#c4000c;
  --red-dark:#9c0009;
  --navy:#1b2440;
  --ink:#222;
  --gray:#9b9b9b;
  --gray-light:#d8d8d8;
  --text:#777;
  --canvas:#eef0f2;
  --ok:#3aa53f;
  --photo:linear-gradient(135deg,#22306a 0%,#0f1634 55%,#2b1228 100%);
  --photo-red:linear-gradient(120deg,#4a0d16 0%,#6b1022 45%,#1c2040 100%);
}
*{margin:0;padding:0;box-sizing:border-box}
html,body{width:692px;height:1200px;overflow:hidden;background:var(--canvas)}
body{position:relative;font-family:"Roboto",sans-serif;color:var(--ink)}
.slide{position:absolute;width:228px;height:127px;background:#fff;overflow:hidden}
.abs{position:absolute}
.photo{position:absolute;background:var(--photo)}
.title{position:absolute;font-family:"Oswald",sans-serif;font-weight:500;font-size:10px;line-height:1.15;color:var(--ink);letter-spacing:-.1px;white-space:nowrap}
.title.light{color:#fff}
.p{position:absolute;font-size:2.6px;line-height:1.5;color:var(--text)}
.p.light{color:#e6e6e6}
.h{position:absolute;font-family:"Oswald",sans-serif;font-weight:500;font-size:3.6px;color:var(--ink);white-space:nowrap}
.brand{position:absolute;left:9px;bottom:6px;display:flex;align-items:center;gap:2px;font-family:"Oswald",sans-serif;font-weight:600;font-size:5px;color:var(--red);letter-spacing:.3px}
.brand::before{content:"";width:4px;height:4px;border-radius:50%;background:var(--red)}
.pg{position:absolute;right:8px;bottom:6px;font-size:3px;color:#ccc}
.num{position:absolute;font-family:"Oswald",sans-serif;font-weight:500;color:var(--ink);white-space:nowrap}
.btn{position:absolute;background:var(--red);color:#fff;font-size:2px;font-weight:700;padding:1px 3px;border-radius:1px}
.dot{position:absolute;width:5px;height:5px;border-radius:50%;background:var(--red);color:#fff;font-size:2px;display:flex;align-items:center;justify-content:center}
.ghost{position:absolute;font-family:"Oswald",sans-serif;font-weight:600;color:#ececec;white-space:nowrap}
.card{position:absolute;background:#fff;box-shadow:0 1px 4px rgba(0,0,0,.18)}
.circ{position:absolute;border-radius:50%;background:var(--photo)}
.vline{position:absolute;border-left:.6px dashed var(--red)}
.hline{position:absolute;border-top:.6px dashed var(--red)}
</style>
</head>
<body>

<!-- Row 1 -->
<section class="slide cover" style="left:2px;top:2px">
  <div class="photo" style="inset:0;background:var(--photo-red)" role="img" aria-label="Esports arena with stage lights"></div>
  <svg class="abs" width="228" height="127" style="left:0;top:0"><polygon points="60,127 150,0 228,0 228,20 140,127" fill="#c4000c" opacity=".25"/></svg>
  <div class="brand" style="top:12px;bottom:auto;font-size:7px">VEXORA</div>
  <div class="title light" style="left:9px;top:55px;font-size:14px">Your Title Goes Here</div>
  <p class="p light" style="left:9px;top:75px;width:105px">A wonderful calm has taken hold of my whole mind, like these sweet evenings of spring which I enjoy with my whole heart. I am alone and feel the charm of this place, made for minds like mine. I am so happy, my dear friend.</p>
  <div class="p light" style="left:9px;top:115px;font-size:2.4px">www.vexora-events.com</div>
</section>

<section class="slide cover" style="left:232px;top:2px">
  <div class="photo" style="inset:0" role="img" aria-label="Esports arena with central stage and crowd"></div>
  <div class="brand" style="left:103px;top:14px;bottom:auto;font-size:7px">VEXORA</div>
  <div class="title light" style="left:0;width:228px;text-align:center;top:60px;font-size:13px">Your Title Goes Here</div>
  <p class="p light" style="left:157px;top:86px;width:62px">A wonderful calm has taken hold of my whole mind, like these sweet evenings of spring which I enjoy with my whole heart. I am alone and feel the charm of this place, made for minds like mine. I am so happy, my dear friend.</p>
</section>

<section class="slide" style="left:462px;top:2px">
  <div class="photo" style="inset:0;background:linear-gradient(135deg,#3a3d48,#15171f 60%,#2a2d36)" role="img" aria-label="Darkened arena seating"></div>
  <svg class="abs" width="228" height="127" style="left:0;top:0"><polygon points="0,0 0,55 70,0" fill="#fff"/><polygon points="0,95 0,127 110,127" fill="#fff"/><polygon points="33,50 60,73 33,73" fill="#c4000c"/></svg>
  <div class="title light" style="left:49px;top:27px;font-size:19px;font-weight:400">INTRODUCTION</div>
  <div class="card" style="left:40px;top:58px;width:145px;height:41px"></div>
  <div class="h" style="left:80px;top:66px;font-size:3.2px">WHAT WE DO</div>
  <p class="p" style="left:80px;top:73px;width:88px">Use agile methods to give a robust summary for high-level reviews. Repeated approaches to shared strategy build team thinking further.</p>
  <div class="abs" style="left:152px;top:104px;display:flex;gap:3px"><i style="width:5px;height:5px;border-radius:50%;background:#fff"></i><i style="width:5px;height:5px;border-radius:50%;background:#fff"></i><i style="width:5px;height:5px;border-radius:50%;background:#fff"></i><i style="width:5px;height:5px;border-radius:50%;background:#fff"></i></div>
  <div class="brand">VEXORA</div><div class="pg">3</div>
</section>

<!-- Row 2 -->
<section class="slide" style="left:2px;top:134px">
  <div class="title" style="left:9px;top:10px">TWO PARAGRAPH SLIDES</div>
  <svg class="abs" width="228" height="127" style="left:0;top:0"><polyline points="62,42 72,51 200,51" fill="none" stroke="#c4000c" stroke-width="1"/><polyline points="62,42 200,42 200,93 115,93 102,80" fill="none" stroke="#c4000c" stroke-width="1"/></svg>
  <div class="card" style="left:28px;top:48px;width:84px;height:56px"></div>
  <div class="h" style="left:34px;top:57px">CUSTOM PART</div>
  <p class="p" style="left:34px;top:64px;width:67px">Use agile methods to give a robust summary for high level reviews. Repeated approaches too.</p>
  <p class="p" style="left:34px;top:82px;width:67px">Shared strategy builds team thinking further for the overall offer.</p>
  <div class="btn" style="left:80px;top:101px">LEARN MORE</div>
  <div class="h" style="left:120px;top:53px">CUSTOM PART</div>
  <p class="p" style="left:120px;top:59px;width:62px">Shared strategy builds team thinking further for the overall offer.</p>
  <div class="num" style="left:125px;top:73px;font-size:4px;color:var(--red)">01.</div>
  <p class="p" style="left:134px;top:73px;width:22px">MOTION Use agile frames</p>
  <div class="num" style="left:153px;top:73px;font-size:4px;color:var(--red)">02.</div>
  <p class="p" style="left:161px;top:73px;width:22px">INTRO Use agile frames</p>
  <div class="brand">VEXORA</div><div class="pg">4</div>
</section>

<section class="slide" style="left:232px;top:134px">
  <div class="photo" style="left:0;top:0;width:100px;height:127px;clip-path:polygon(0 0,80% 0,100% 100%,0 100%)" role="img" aria-label="Colourful esports stage with screens"></div>
  <div class="abs" style="left:26px;top:12px;color:#fff;font-size:9px">+</div>
  <div class="ghost" style="left:210px;top:30px;font-size:20px;writing-mode:vertical-rl;transform:rotate(180deg)">GAMERS</div>
  <div class="title" style="left:113px;top:30px">EVENT BENEFITS</div>
  <p class="p" style="left:113px;top:47px;width:95px">Lorem ipsum dolor sit amet, consectetur adipiscing elit sed do eiusmod tempor incididunt ut labore dolore magna aliqua.</p>
  <div class="abs" style="left:45px;top:81px;width:84px;height:33px;background:var(--red)"></div>
  <div class="abs" style="left:132px;top:81px;width:51px;height:33px;background:var(--red-dark)"></div>
  <p class="p light" style="left:55px;top:88px;width:32px"><b>First Benefits</b><br>Lorem ipsum dolor sit amet adipiscing</p>
  <p class="p light" style="left:90px;top:88px;width:32px"><b>Second Benefits</b><br>Lorem ipsum dolor sit amet adipiscing</p>
  <p class="p light" style="left:140px;top:88px;width:36px"><b>Third Benefits</b><br>Lorem ipsum dolor sit amet adipiscing</p>
  <div class="pg">5</div>
</section>

<section class="slide" style="left:462px;top:134px">
  <div class="photo" style="left:0;top:0;width:228px;height:80px;clip-path:polygon(0 0,100% 0,100% 60%,60% 100%,0 80%);background:linear-gradient(135deg,#2a3048,#131826)" role="img" aria-label="Arena crowd in dim light"></div>
  <div class="ghost" style="left:210px;top:10px;font-size:10px;color:#4a4f60;writing-mode:vertical-rl">Gamers</div>
  <div class="title light" style="left:29px;top:24px">EVENTS PROFILES</div>
  <p class="p light" style="left:29px;top:40px;width:110px">Lorem ipsum dolor sit amet, consectetur adipiscing elit, sed do eiusmod tempor incididunt ut labore dolore magna aliqua, enim minim dolor amet.</p>
  <div class="abs" style="left:29px;top:104px;width:3px;height:10px;background:var(--red)"></div>
  <div class="num" style="left:33px;top:96px;font-size:17px">12</div>
  <p class="p" style="left:65px;top:101px;width:40px">Lorem ipsum dolor sit amet, consectetur adipiscing elit sed do eiusmod</p>
  <div class="abs" style="left:114px;top:104px;width:3px;height:10px;background:var(--red)"></div>
  <div class="num" style="left:118px;top:96px;font-size:17px">17</div>
  <p class="p" style="left:150px;top:101px;width:40px">Lorem ipsum dolor sit amet, consectetur adipiscing elit sed do eiusmod</p>
  <div class="brand">VEXORA</div>
</section>

<!-- Row 3 -->
<section class="slide" style="left:2px;top:266px">
  <svg class="abs" width="228" height="127" style="left:0;top:0"><polygon points="228,0 228,40 190,40 170,40 205,0" fill="#c4000c"/><polygon points="165,12 228,12 228,60 165,60" fill="#c4000c"/></svg>
  <div class="ghost" style="left:0;top:30px;font-size:20px;writing-mode:vertical-rl;transform:rotate(180deg)">GAMERS</div>
  <div class="title" style="left:28px;top:24px">EVENT PRODUCTS</div>
  <p class="p" style="left:28px;top:52px;width:80px">Lorem ipsum dolor sit amet, consectetur adipiscing elit, sed do eiusmod tempor incididunt ut labore dolore</p>
  <p class="p" style="left:28px;top:73px;width:50px">Lorem ipsum dolor sit amet, consectetur adipiscing elit, sed do</p>
  <div class="num" style="left:28px;top:90px;font-size:7px">25%</div>
  <p class="p" style="left:50px;top:91px;width:40px;font-size:3px">Discount<br>For Those Products</p>
  <div class="photo" style="left:130px;top:30px;width:32px;height:32px" role="img" aria-label="Event stage photo"></div>
  <div class="photo" style="left:167px;top:30px;width:32px;height:32px" role="img" aria-label="Event stage photo"></div>
  <div class="photo" style="left:130px;top:66px;width:32px;height:32px" role="img" aria-label="Event stage photo"></div>
  <div class="photo" style="left:167px;top:66px;width:32px;height:32px" role="img" aria-label="Event stage photo"></div>
  <div class="brand">VEXORA</div><div class="pg">7</div>
</section>

<section class="slide" style="left:232px;top:266px">
  <svg class="abs" width="228" height="127" style="left:0;top:0"><polygon points="185,0 228,0 228,20 90,127 75,127" fill="#d0d0d0"/></svg>
  <div class="photo" style="left:10px;top:12px;width:85px;height:100px;background:linear-gradient(135deg,#d21018,#8c0a10)" role="img" aria-label="Red-toned event crowd photo"></div>
  <div class="photo" style="left:97px;top:28px;width:125px;height:99px;clip-path:polygon(0 0,100% 0,100% 100%,0 100%)" role="img" aria-label="Blue-lit esports arena"></div>
  <p class="p light" style="left:43px;top:79px;width:45px">A wonderful calm has taken hold of my whole mind, like sweet spring evenings I enjoy with all my heart.</p>
  <div class="title light" style="left:108px;top:52px;font-size:15px;line-height:1.2">SLIDE BREAK<br>TITLE GOES HERE</div>
  <div class="brand">VEXORA</div>
</section>

<section class="slide" style="left:462px;top:266px">
  <div class="title" style="left:9px;top:10px">BUSINESS STRATEGY SLIDE</div>
  <p class="p" style="left:9px;top:27px;width:160px">Use agile methods to give a robust summary for high level reviews. Repeated approaches to shared strategy build team thinking further for the overall offer.</p>
  <div class="dot" style="left:26px;top:51px">01</div><div class="h" style="left:44px;top:50px">CUSTOM PART</div><p class="p" style="left:44px;top:56px;width:36px">Use agile methods to give a robust summary for high level reviews.</p>
  <div class="dot" style="left:88px;top:51px">02</div><div class="h" style="left:106px;top:50px">NEW ENGINE</div><p class="p" style="left:106px;top:56px;width:36px">Use agile methods to give a robust summary for high level reviews.</p>
  <div class="dot" style="left:149px;top:51px">03</div><div class="h" style="left:167px;top:50px">DEALER</div><p class="p" style="left:167px;top:56px;width:36px">Use agile methods to give a robust summary for high level reviews.</p>
  <div class="dot" style="left:26px;top:80px">04</div><div class="h" style="left:44px;top:79px">SAFETY GEAR</div><p class="p" style="left:44px;top:85px;width:36px">Use agile methods to give a robust summary for high level reviews.</p>
  <div class="dot" style="left:88px;top:80px">05</div><div class="h" style="left:106px;top:79px">2 NEW SYSTEM</div><p class="p" style="left:106px;top:85px;width:36px">Use agile methods to give a robust summary for high level reviews.</p>
  <div class="dot" style="left:149px;top:80px">06</div><div class="h" style="left:167px;top:79px">AUTO PARTS ONE</div><p class="p" style="left:167px;top:85px;width:36px">Use agile methods to give a robust summary for high level reviews.</p>
  <div class="brand">VEXORA</div><div class="pg">9</div>
</section>

<!-- Row 4 -->
<section class="slide" style="left:2px;top:398px">
  <div class="photo" style="inset:0;background:linear-gradient(135deg,#232a44,#11152a 60%,#1e2238)" role="img" aria-label="Dim arena seating"></div>
  <svg class="abs" width="228" height="127" style="left:0;top:0"><polygon points="228,40 228,127 150,127" fill="#c4000c" opacity=".7"/></svg>
  <div class="brand" style="left:12px;top:16px;bottom:auto;font-size:7px">VEXORA</div>
  <div class="abs" style="left:78px;top:83px;font-family:Oswald,sans-serif;font-weight:600;font-style:normal;font-size:20px;color:var(--red)">SECTION <span style="color:#fff;font-size:13px">BREAK</span></div>
</section>

<section class="slide" style="left:232px;top:398px">
  <div class="title" style="left:9px;top:10px;line-height:1.25">TIMELINE<br>SLIDE DESIGN</div>
  <div class="num" style="left:119px;top:33px;font-size:11px">01</div>
  <div class="h" style="left:80px;top:50px;text-align:right;width:35px">01.<br>SERVICE ONE</div>
  <p class="p" style="left:45px;top:65px;width:70px;text-align:right">Use agile methods to give a robust summary for high level reviews.</p>
  <div class="vline" style="left:90px;top:62px;height:14px"></div>
  <div class="hline" style="left:90px;top:76px;width:47px"></div>
  <div class="num" style="left:93px;top:78px;font-size:11px">02</div>
  <div class="vline" style="left:136px;top:76px;height:17px"></div>
  <div class="h" style="left:134px;top:82px">02.<br>SERVICE TWO</div>
  <p class="p" style="left:134px;top:92px;width:45px">Use agile methods to give a robust summary for high level reviews.</p>
  <div class="hline" style="left:90px;top:107px;width:47px"></div>
  <div class="vline" style="left:90px;top:107px;height:20px"></div>
  <div class="brand">VEXORA</div><div class="pg">11</div>
</section>

<section class="slide" style="left:462px;top:398px">
  <div class="hline" style="left:90px;top:8px;width:46px"></div><div class="vline" style="left:90px;top:0;height:8px"></div>
  <div class="circ" style="left:100px;top:13px;width:24px;height:24px" role="img" aria-label="Event photo"></div>
  <div class="num" style="left:93px;top:12px;font-size:11px">03</div>
  <div class="card" style="left:128px;top:15px;width:60px;height:46px"></div>
  <div class="h" style="left:134px;top:20px">03.<br>SERVICE THREE</div>
  <p class="p" style="left:134px;top:31px;width:44px">Use agile methods to give a robust summary for high level reviews.</p>
  <div class="btn" style="left:166px;top:53px">LEARN MORE</div>
  <div class="vline" style="left:90px;top:45px;height:10px"></div><div class="hline" style="left:90px;top:55px;width:46px"></div>
  <div class="circ" style="left:100px;top:50px;width:24px;height:24px" role="img" aria-label="Event photo"></div>
  <div class="num" style="left:121px;top:49px;font-size:11px">04</div>
  <p class="p" style="left:26px;top:60px;width:50px;text-align:right">Use agile methods to give a robust summary for high level reviews.</p>
  <div class="h" style="left:70px;top:60px">04.<br>SERVICE FOUR</div>
  <div class="vline" style="left:136px;top:80px;height:10px"></div><div class="hline" style="left:90px;top:80px;width:46px"></div>
  <div class="circ" style="left:100px;top:90px;width:24px;height:24px" role="img" aria-label="Event photo"></div>
  <div class="num" style="left:93px;top:88px;font-size:11px">05</div>
  <div class="h" style="left:134px;top:94px">05.<br>SERVICE FIVE</div>
  <p class="p" style="left:162px;top:94px;width:40px">Use agile methods to give a robust summary for high level reviews.</p>
  <div class="hline" style="left:90px;top:119px;width:46px"></div><div class="vline" style="left:90px;top:119px;height:8px"></div>
  <div class="brand">VEXORA</div><div class="pg">12</div>
</section>

<!-- Row 5 -->
<section class="slide" style="left:2px;top:530px">
  <div class="vline" style="left:90px;top:0;height:8px"></div><div class="hline" style="left:90px;top:8px;width:46px"></div><div class="vline" style="left:136px;top:8px;height:8px"></div>
  <div class="circ" style="left:102px;top:13px;width:24px;height:24px" role="img" aria-label="Event photo"></div>
  <div class="num" style="left:122px;top:12px;font-size:11px">06</div>
  <div class="h" style="left:36px;top:14px;width:34px;text-align:right">06.<br>SERVICE SIX</div>
  <p class="p" style="left:24px;top:25px;width:46px;text-align:right">Use agile methods to give a robust summary for high level reviews.</p>
  <div class="vline" style="left:90px;top:40px;height:8px"></div><div class="hline" style="left:90px;top:48px;width:46px"></div>
  <div class="circ" style="left:102px;top:52px;width:24px;height:24px" role="img" aria-label="Event photo"></div>
  <div class="num" style="left:92px;top:51px;font-size:11px">07</div>
  <div class="h" style="left:135px;top:58px">07.<br>SERVICE SEVEN</div>
  <p class="p" style="left:161px;top:58px;width:42px">Use agile methods to give a robust summary for high level reviews.</p>
  <div class="vline" style="left:136px;top:80px;height:8px"></div><div class="hline" style="left:90px;top:88px;width:46px"></div>
  <div class="h" style="left:100px;top:97px;font-size:4px">END TIME LINE</div>
  <div class="brand">VEXORA</div><div class="pg">13</div>
</section>

<section class="slide" style="left:232px;top:530px">
  <div class="photo" style="left:0;top:0;width:94px;height:127px" role="img" aria-label="Arena stage photo"></div>
  <div class="ghost" style="left:6px;top:96px;font-size:26px;color:#3a4468">14</div>
  <div class="card" style="left:37px;top:16px;width:84px;height:46px"></div>
  <svg class="abs" width="84" height="46" style="left:37px;top:16px">
    <g font-size="2" fill="#bbb"><text x="6" y="8">Food 4</text><text x="6" y="16">Food 3</text><text x="6" y="24">Food 2</text><text x="6" y="32">Food 1</text></g>
    <rect x="18" y="6" width="30" height="2.4" fill="#1b2440"/><rect x="48" y="6" width="12" height="2.4" fill="#c4000c"/><rect x="60" y="6" width="4" height="2.4" fill="#bbb"/>
    <rect x="18" y="14" width="26" height="2.4" fill="#1b2440"/><rect x="44" y="14" width="12" height="2.4" fill="#c4000c"/><rect x="56" y="14" width="8" height="2.4" fill="#bbb"/>
    <rect x="18" y="22" width="20" height="2.4" fill="#1b2440"/><rect x="38" y="22" width="14" height="2.4" fill="#c4000c"/><rect x="52" y="22" width="14" height="2.4" fill="#bbb"/>
    <rect x="18" y="30" width="28" height="2.4" fill="#1b2440"/><rect x="46" y="30" width="10" height="2.4" fill="#c4000c"/><rect x="56" y="30" width="4" height="2.4" fill="#bbb"/>
  </svg>
  <div class="card" style="left:37px;top:66px;width:84px;height:46px"></div>
  <svg class="abs" width="84" height="46" style="left:37px;top:66px">
    <g font-size="2" fill="#bbb"><text x="6" y="8">Food 4</text><text x="6" y="16">Food 3</text><text x="6" y="24">Food 2</text><text x="6" y="32">Food 1</text></g>
    <rect x="18" y="6" width="20" height="2.4" fill="#1b2440"/><rect x="38" y="6" width="26" height="2.4" fill="#bbb"/>
    <rect x="18" y="14" width="10" height="2.4" fill="#1b2440"/><rect x="28" y="14" width="16" height="2.4" fill="#c4000c"/><rect x="44" y="14" width="12" height="2.4" fill="#bbb"/>
    <rect x="18" y="22" width="32" height="2.4" fill="#1b2440"/><rect x="50" y="22" width="8" height="2.4" fill="#c4000c"/><rect x="58" y="22" width="12" height="2.4" fill="#bbb"/>
    <rect x="18" y="30" width="36" height="2.4" fill="#1b2440"/><rect x="54" y="30" width="14" height="2.4" fill="#c4000c"/>
  </svg>
  <div class="title" style="left:144px;top:28px;line-height:1.25">BUSINESS DATA<br>REPORT</div>
  <p class="p" style="left:144px;top:55px;width:56px">Use agile methods to give a robust summary for high level reviews. Repeated approaches to shared strategy build team thinking further for the overall offer.</p>
  <p class="p" style="left:144px;top:82px;color:var(--red);font-style:italic">"At the end of the day, going forward"</p>
  <div class="btn" style="left:144px;top:90px">LEARN MORE</div>
  <div class="pg">14</div>
</section>

<section class="slide" style="left:462px;top:530px">
  <div class="title" style="left:21px;top:30px;line-height:1.25">2019 DECORATION<br>STATISTIC</div>
  <p class="p" style="left:21px;top:57px;width:68px">Use agile methods to give a robust summary for high level reviews. Repeated approaches to shared strategy build team thinking further for the overall value offer.</p>
  <p class="p" style="left:21px;top:83px;color:var(--red);font-style:italic">"At the end of the day, going forward"</p>
  <div class="btn" style="left:21px;top:92px">LEARN MORE</div>
  <div class="photo" style="left:94px;top:0;width:134px;height:127px" role="img" aria-label="Blue-lit arena background"></div>
  <svg class="abs" width="134" height="127" style="left:94px;top:0">
    <g font-size="2" fill="#ccc"><text x="37" y="27">JAN</text><text x="59" y="27">FEB</text><text x="81" y="27">MAR</text><text x="103" y="27">APR</text>
    <text x="18" y="33">100%</text><text x="18" y="43">80%</text><text x="18" y="53">60%</text><text x="18" y="63">40%</text><text x="18" y="73">20%</text><text x="18" y="80">0%</text></g>
    <rect x="36" y="31" width="7" height="48" fill="#7a7f8e"/><rect x="36" y="31" width="7" height="8" fill="#fff"/>
    <rect x="58" y="31" width="7" height="48" fill="#7a7f8e"/><rect x="58" y="31" width="7" height="10" fill="#fff"/>
    <rect x="80" y="31" width="7" height="48" fill="#7a7f8e"/><rect x="80" y="31" width="7" height="13" fill="#fff"/>
    <rect x="102" y="31" width="7" height="48" fill="#7a7f8e"/><rect x="102" y="31" width="7" height="17" fill="#fff"/>
  </svg>
  <div class="abs" style="left:114px;top:86px;width:30px;height:24px;background:var(--red);color:#fff;font-size:2.4px;font-weight:700;display:flex;align-items:flex-end;justify-content:center;padding-bottom:3px">CUSTOM PART</div>
  <div class="abs" style="left:146px;top:86px;width:63px;height:24px;background:#fff"></div>
  <div class="h" style="left:150px;top:90px;color:var(--red)">27,000+</div>
  <p class="p" style="left:150px;top:96px;width:55px">Use agile methods to give a robust summary for high level reviews.</p>
  <div class="brand">VEXORA</div>
</section>

<!-- Row 6 -->
<section class="slide" style="left:2px;top:662px">
  <div class="title" style="left:9px;top:10px">EUROPE MAP SLIDE</div>
  <div class="abs" style="left:110px;top:10px;width:118px;height:110px;background:linear-gradient(100deg,#e2e2e2 45%,#c4000c 70%);clip-path:polygon(20% 10%,60% 0,100% 5%,100% 100%,40% 95%,15% 70%,25% 40%)" role="img" aria-label="Map of Europe with eastern region highlighted"></div>
  <div class="abs" style="left:148px;top:12px;width:26px;height:26px;border-radius:50%;background:#fff;box-shadow:0 1px 3px rgba(0,0,0,.2)"></div>
  <div class="num" style="left:155px;top:16px;font-size:6px;color:var(--red)">2019</div><div class="p" style="left:158px;top:24px">Text</div>
  <div class="abs" style="left:190px;top:76px;width:28px;height:28px;border-radius:50%;background:#fff;box-shadow:0 1px 3px rgba(0,0,0,.2)"></div>
  <div class="num" style="left:200px;top:80px;font-size:6px">12</div><div class="p" style="left:200px;top:89px">Text</div>
  <div class="card" style="left:30px;top:78px;width:70px;height:22px;transform:skewX(-25deg)"></div>
  <div class="num" style="left:47px;top:81px;font-size:5px;color:var(--red)">$320K</div>
  <p class="p" style="left:47px;top:90px">Lorem ipsum dolor</p>
  <div class="brand">VEXORA</div><div class="pg">16</div>
</section>

<section class="slide pricing" style="left:232px;top:662px">
  <div class="title" style="left:9px;top:10px">PRICING</div>
  <div class="abs" style="left:0;top:80px;width:228px;height:47px;background:var(--red)"></div>
  <svg class="abs" width="228" height="127" style="left:0;top:0">
    <g font-family="Oswald,sans-serif" font-size="3.2" font-weight="500">
      <g><rect x="24" y="27" width="180" height="14" fill="#fff" filter="drop-shadow(0 .5px 1px rgba(0,0,0,.15))"/><text x="52" y="36" fill="#222">SED COMMODO MI NULLA,</text><text x="108" y="36" fill="#999" font-size="2.4">Price</text><text x="117" y="36" fill="#222">$400.00</text><text x="145" y="36" fill="#999" font-size="2.4">Quantity</text><text x="160" y="36" fill="#222">1</text><text x="180" y="36" fill="#222" font-size="2.6">LEARN MORE</text></g>
      <g><rect x="24" y="45" width="180" height="14" fill="#fff" filter="drop-shadow(0 .5px 1px rgba(0,0,0,.15))"/><text x="52" y="54" fill="#222">SED COMMODO MI NULLA,</text><text x="108" y="54" fill="#999" font-size="2.4">Price</text><text x="117" y="54" fill="#222">$400.00</text><text x="145" y="54" fill="#999" font-size="2.4">Quantity</text><text x="160" y="54" fill="#222">1</text><text x="180" y="54" fill="#222" font-size="2.6">LEARN MORE</text></g>
      <g><rect x="24" y="63" width="180" height="14" fill="#fff" filter="drop-shadow(0 .5px 1px rgba(0,0,0,.15))"/><text x="52" y="72" fill="#222">SED COMMODO MI NULLA,</text><text x="108" y="72" fill="#999" font-size="2.4">Price</text><text x="117" y="72" fill="#222">$400.00</text><text x="145" y="72" fill="#999" font-size="2.4">Quantity</text><text x="160" y="72" fill="#222">1</text><text x="180" y="72" fill="#222" font-size="2.6">LEARN MORE</text></g>
      <g><rect x="24.5" y="81" width="179" height="14" fill="#fff" stroke="#c4000c" stroke-width=".6"/><text x="52" y="90" fill="#c4000c">SED COMMODO MI NULLA,</text><text x="108" y="90" fill="#999" font-size="2.4">Price</text><text x="117" y="90" fill="#c4000c">$400.00</text><text x="145" y="90" fill="#999" font-size="2.4">Quantity</text><text x="160" y="90" fill="#c4000c">1</text><text x="180" y="90" fill="#c4000c" font-size="2.6">LEARN MORE</text></g>
      <g><rect x="24" y="99" width="180" height="14" fill="#fff"/><text x="52" y="108" fill="#222">SED COMMODO MI NULLA,</text><text x="108" y="108" fill="#999" font-size="2.4">Price</text><text x="117" y="108" fill="#222">$400.00</text><text x="145" y="108" fill="#999" font-size="2.4">Quantity</text><text x="160" y="108" fill="#222">1</text><text x="180" y="108" fill="#222" font-size="2.6">LEARN MORE</text></g>
    </g>
  </svg>
</section>

<section class="slide" style="left:462px;top:662px">
  <div class="title" style="left:9px;top:10px">OUR TABLE</div>
  <svg class="abs" width="228" height="127" style="left:0;top:0">
    <rect x="20" y="32" width="187" height="13" fill="#c4000c"/><text x="113" y="40" font-size="3" fill="#fff" text-anchor="middle">TABLE TITLE GOES HERE</text>
    <rect x="20" y="45" width="187" height="67" fill="#fff" filter="drop-shadow(0 1px 2px rgba(0,0,0,.15))"/>
    <rect x="20" y="45" width="36" height="17" fill="#c4000c"/><rect x="20" y="62" width="36" height="17" fill="#ccc"/><rect x="20" y="79" width="36" height="17" fill="#9b9b9b"/><rect x="20" y="96" width="36" height="16" fill="#c4000c"/>
    <g font-family="Oswald,sans-serif" font-size="2.8" fill="#fff" text-anchor="middle"><text x="38" y="53">STANDARD</text><text x="38" y="57">SERVICE</text><text x="38" y="70">BRONZE</text><text x="38" y="74">SERVICE</text><text x="38" y="87">SILVER</text><text x="38" y="91">SERVICE</text><text x="38" y="104">GOLD</text><text x="38" y="108">SERVICE</text></g>
    <g font-size="2.4" fill="#777"><text x="63" y="53"><tspan font-style="italic" fill="#222">I am alone, and feel the charm</tspan> of being in this spot, made for</text><text x="63" y="57">minds like mine, possession</text>
    <text x="63" y="70"><tspan font-style="italic" fill="#222">I am alone, and feel the charm</tspan> of being in this spot, made for</text><text x="63" y="74">minds like mine, possession</text>
    <text x="63" y="87"><tspan font-style="italic" fill="#222">I am alone, and feel the charm</tspan> of being in this spot, made for</text><text x="63" y="91">minds like mine, possession</text>
    <text x="63" y="104"><tspan font-style="italic" fill="#222">I am alone, and feel the charm</tspan> of being in this spot, made for</text><text x="63" y="108">minds like mine, possession</text></g>
    <g font-family="Oswald,sans-serif" font-size="5" fill="#c4000c"><text x="180" y="56">$45.99</text><text x="180" y="73" fill="#ccc">$75.99</text><text x="180" y="90" fill="#999">$85.99</text><text x="180" y="106">$95.99</text></g>
  </svg>
  <div class="brand">VEXORA</div><div class="pg">18</div>
</section>

<!-- Row 7 -->
<section class="slide" style="left:2px;top:794px">
  <div class="title" style="left:9px;top:10px">OUR EVENT</div>
  <p class="p" style="left:26px;top:51px;width:56px;text-align:right"><i style="font-size:3.4px;color:#555">A wonderful calm has taken</i><br>A wonderful calm has taken hold of my whole mind, like these sweet evenings of spring which I enjoy with my whole heart. I am alone and feel the charm of this place, made for minds like mine. I am so happy, my dear friend, so absorbed in quiet being that my art suffers, while the lovely valley teems with mist around me and the sun rests on the dark forest.</p>
  <div class="photo" style="left:89px;top:6px;width:36px;height:36px" role="img" aria-label="Event photo"></div>
  <div class="abs" style="left:89px;top:46px;width:36px;height:36px;background:var(--red)"></div>
  <div class="photo" style="left:89px;top:86px;width:36px;height:36px" role="img" aria-label="Event photo"></div>
  <div class="photo" style="left:129px;top:0;width:36px;height:22px" role="img" aria-label="Event photo"></div>
  <div class="photo" style="left:129px;top:26px;width:36px;height:36px" role="img" aria-label="Event photo"></div>
  <div class="abs" style="left:129px;top:66px;width:36px;height:36px;background:#ddd"></div>
  <div class="photo" style="left:129px;top:106px;width:36px;height:21px" role="img" aria-label="Event photo"></div>
  <div class="photo" style="left:169px;top:6px;width:36px;height:36px" role="img" aria-label="Event photo"></div>
  <div class="abs" style="left:169px;top:46px;width:36px;height:36px;background:#aaa"></div>
  <div class="photo" style="left:169px;top:86px;width:36px;height:36px" role="img" aria-label="Event photo"></div>
  <div class="abs" style="left:101px;top:53px;width:11px;height:11px;border-radius:50%;background:#fff"></div>
  <p class="p light" style="left:91px;top:69px;width:32px;text-align:center">A wonderful calm has taken</p>
  <div class="abs" style="left:142px;top:73px;width:9px;height:9px;border:.8px solid #888;border-radius:50%"></div>
  <p class="p" style="left:131px;top:86px;width:32px;text-align:center">A wonderful calm has taken</p>
  <div class="abs" style="left:182px;top:52px;width:11px;height:11px;border-radius:50%;background:#ccc"></div>
  <p class="p light" style="left:171px;top:69px;width:32px;text-align:center">A wonderful calm has taken</p>
  <div class="brand">VEXORA</div>
</section>

<section class="slide" style="left:232px;top:794px">
  <div class="photo" style="left:0;top:0;width:113px;height:127px;background:linear-gradient(135deg,#21306a,#0e1532 55%,#3a4a8a)" role="img" aria-label="Smartphone held over an esports arena"></div>
  <div class="abs" style="left:33px;top:14px;width:50px;height:112px;border:2px solid #e8e8e8;border-radius:7px"></div>
  <div class="num" style="left:124px;top:14px;font-size:17px;color:var(--red)">01</div>
  <div class="h" style="left:150px;top:18px">Option One</div>
  <p class="p" style="left:150px;top:26px;width:65px">A wonderful calm has taken hold of my whole mind, like sweet evenings of spring I enjoy with my whole heart.</p>
  <div class="abs" style="left:103px;top:49px;width:103px;height:34px;background:var(--red)"></div>
  <div class="num" style="left:110px;top:52px;font-size:17px;color:#fff">02</div>
  <div class="h" style="left:136px;top:56px;color:#fff">Option Two</div>
  <p class="p light" style="left:136px;top:63px;width:65px">A wonderful calm has taken hold of my whole mind, like sweet evenings of spring I enjoy with my whole heart.</p>
  <div class="num" style="left:124px;top:88px;font-size:17px;color:var(--red)">03</div>
  <div class="h" style="left:150px;top:94px">Option Three</div>
  <p class="p" style="left:150px;top:102px;width:65px">A wonderful calm has taken hold of my whole mind, like sweet evenings of spring I enjoy with my whole heart.</p>
</section>

<section class="slide" style="left:462px;top:794px">
  <div class="title" style="left:9px;top:10px;text-transform:none">Infographic Table slide</div>
  <svg class="abs" width="228" height="127" style="left:0;top:0">
    <rect x="20" y="41" width="184" height="59" fill="#f0f0f0"/>
    <g fill="#8f8f8f"><rect x="98" y="36" width="26" height="6"/><rect x="125" y="36" width="26" height="6"/><rect x="152" y="36" width="26" height="6"/><rect x="179" y="36" width="26" height="6"/></g>
    <g font-size="2.6" fill="#fff" text-anchor="middle" font-weight="700"><text x="111" y="40">Your Text</text><text x="138" y="40">Your Text</text><text x="165" y="40">Your Text</text><text x="192" y="40">Your Text</text></g>
    <g font-size="2" fill="#aaa"><text x="24" y="47">Like these sweet mornings</text><text x="24" y="55.5">spring which I enjoy</text><text x="24" y="64">with my whole heart</text><text x="24" y="72.5">I am alone, and feel the charm of being</text><text x="24" y="81">A wonderful calm has taken hold</text><text x="24" y="89.5">I am so happy</text><text x="24" y="98">which was made for minds like mine</text></g>
    <g stroke="#fff" stroke-width=".5"><line x1="20" y1="50" x2="204" y2="50"/><line x1="20" y1="58.5" x2="204" y2="58.5"/><line x1="20" y1="67" x2="204" y2="67"/><line x1="20" y1="75.5" x2="204" y2="75.5"/><line x1="20" y1="84" x2="204" y2="84"/><line x1="20" y1="92.5" x2="204" y2="92.5"/></g>
    <defs>
      <g id="tick"><circle r="2.6" fill="#3aa53f"/><path d="M-1.2 0 L-.3 1 L1.3 -1" stroke="#fff" stroke-width=".6" fill="none"/></g>
      <g id="cross"><circle r="2.6" fill="#c4000c"/><path d="M-1 -1 L1 1 M1 -1 L-1 1" stroke="#fff" stroke-width=".6"/></g>
    </defs>
    <use href="#tick" x="111" y="45.5"/><use href="#tick" x="138" y="45.5"/><use href="#cross" x="165" y="45.5"/><use href="#cross" x="192" y="45.5"/>
    <use href="#tick" x="138" y="54"/>
    <use href="#tick" x="111" y="62.5"/><use href="#tick" x="138" y="62.5"/><use href="#tick" x="165" y="62.5"/><use href="#tick" x="192" y="62.5"/>
    <use href="#cross" x="138" y="71"/><use href="#cross" x="165" y="71"/>
    <use href="#tick" x="111" y="79.5"/><use href="#tick" x="138" y="79.5"/><use href="#cross" x="192" y="79.5"/>
    <use href="#cross" x="111" y="88"/><use href="#cross" x="165" y="88"/><use href="#tick" x="192" y="88"/>
    <use href="#cross" x="138" y="96.5"/><use href="#tick" x="165" y="96.5"/><use href="#tick" x="192" y="96.5"/>
    <use href="#tick" x="118" y="108"/><text x="122" y="109" font-size="2.6" fill="#999">Your Text Goes Here</text>
    <use href="#cross" x="164" y="108"/><text x="168" y="109" font-size="2.6" fill="#999">Your Text Goes Here</text>
  </svg>
  <div class="brand">VEXORA</div><div class="pg">21</div>
</section>

<!-- Row 8 -->
<section class="slide" style="left:2px;top:925px">
  <div class="title" style="left:9px;top:10px;text-transform:none">Matrix diagram slide</div>
  <div class="btn" style="left:101px;top:31px;font-size:2.4px;border-radius:3px;padding:1px 6px">Learn More</div>
  <svg class="abs" width="228" height="127" style="left:0;top:0">
    <rect x="12" y="44" width="61" height="30" fill="#c4000c"/><rect x="12" y="74" width="61" height="30" fill="#8f8f8f"/>
    <rect x="155" y="44" width="61" height="30" fill="#aaa"/><rect x="155" y="74" width="61" height="30" fill="#8f8f8f"/>
    <circle cx="42" cy="44" r="4" fill="#c4000c" stroke="#fff" stroke-width=".8"/><text x="42" y="45.3" font-size="3.4" fill="#fff" text-anchor="middle">01</text>
    <circle cx="42" cy="74" r="4" fill="#8f8f8f" stroke="#fff" stroke-width=".8"/><text x="42" y="75.3" font-size="3.4" fill="#fff" text-anchor="middle">02</text>
    <circle cx="186" cy="44" r="4" fill="#aaa" stroke="#fff" stroke-width=".8"/><text x="186" y="45.3" font-size="3.4" fill="#fff" text-anchor="middle">03</text>
    <circle cx="186" cy="74" r="4" fill="#8f8f8f" stroke="#fff" stroke-width=".8"/><text x="186" y="75.3" font-size="3.4" fill="#fff" text-anchor="middle">04</text>
    <g font-size="3.2" fill="#fff" text-anchor="middle" font-family="Oswald,sans-serif"><text x="42" y="55">Your Title Text Here</text><text x="42" y="85">Your Title Text Here</text><text x="186" y="55">Your Title Text Here</text><text x="186" y="85">Your Title Text Here</text></g>
    <g font-size="2.2" fill="#f2f2f2" text-anchor="middle"><text x="42" y="60">A wonderful calm has taken</text><text x="42" y="63">hold of my whole mind, like these</text><text x="42" y="90">A wonderful calm has taken</text><text x="42" y="93">hold of my whole mind, like these</text><text x="186" y="60">A wonderful calm has taken</text><text x="186" y="63">hold of my whole mind, like these</text><text x="186" y="90">A wonderful calm has taken</text><text x="186" y="93">hold of my whole mind, like these</text></g>
    <line x1="114" y1="38" x2="114" y2="110" stroke="#bbb" stroke-width=".5"/><line x1="80" y1="74" x2="148" y2="74" stroke="#bbb" stroke-width=".5"/>
    <rect x="84" y="44" width="27" height="27" rx="3" fill="#c4000c"/><rect x="117" y="44" width="27" height="27" rx="3" fill="#bbb"/>
    <rect x="84" y="77" width="27" height="27" rx="3" fill="#aaa"/><rect x="117" y="77" width="27" height="27" rx="3" fill="#8f8f8f"/>
    <circle cx="97.5" cy="57.5" r="5" fill="none" stroke="#fff" stroke-width=".8"/>
    <path d="M126 52 h9 v3 a4.5 4.5 0 0 1 -9 0z M130.5 59.5 v3 M127.5 63 h6" fill="none" stroke="#fff" stroke-width=".8"/>
    <path d="M91 90.5 h13 M92 87.5 v6 M103 87.5 v6" stroke="#fff" stroke-width="1"/>
    <path d="M127 93 h9 v-3 a3 3 0 0 0 -6 0" fill="none" stroke="#fff" stroke-width=".8"/>
  </svg>
  <div class="brand">VEXORA</div><div class="pg">22</div>
</section>

<section class="slide" style="left:232px;top:925px">
  <div class="title" style="left:9px;top:10px">INFOGRAPHIC</div>
  <svg class="abs" width="228" height="127" style="left:0;top:0">
    <g fill="none" stroke-width="4">
      <polygon points="34,64 43,49 60,49 69,64 60,79 43,79" stroke="#c4000c"/>
      <polygon points="76,64 85,49 102,49 111,64 102,79 85,79" stroke="#1b2440"/>
      <polygon points="118,64 127,49 144,49 153,64 144,79 127,79" stroke="#1b2440"/>
      <polygon points="160,64 169,49 186,49 195,64 186,79 169,79" stroke="#bbb"/>
    </g>
    <g font-size="2.6" fill="#888" text-anchor="middle"><text x="51.5" y="65">STEP 01</text><text x="93.5" y="65">STEP 02</text><text x="135.5" y="65">STEP 03</text><text x="177.5" y="65">STEP 04</text></g>
    <g stroke="#c4000c" stroke-width=".4"><line x1="93.5" y1="45" x2="93.5" y2="35"/><line x1="177.5" y1="45" x2="177.5" y2="35"/><line x1="51.5" y1="83" x2="51.5" y2="92"/><line x1="135.5" y1="83" x2="135.5" y2="92"/></g>
  </svg>
  <div class="h" style="left:84px;top:14px;color:var(--red)">NEW COLOR</div>
  <p class="p" style="left:72px;top:20px;width:44px;text-align:center">Sed ut perspiciatis unde omnis iste natus error sit voluptatem</p>
  <div class="h" style="left:166px;top:14px;color:#999">PRESENTATION</div>
  <p class="p" style="left:156px;top:20px;width:44px;text-align:center">Sed ut perspiciatis unde omnis iste natus error sit voluptatem</p>
  <div class="h" style="left:40px;top:96px;color:var(--red)">AUTOMOTIVE</div>
  <p class="p" style="left:30px;top:102px;width:44px;text-align:center">Sed ut perspiciatis unde omnis iste natus error sit voluptatem</p>
  <div class="h" style="left:124px;top:96px;color:var(--red)">NEW DESIGN</div>
  <p class="p" style="left:114px;top:102px;width:44px;text-align:center">Sed ut perspiciatis unde omnis iste natus error sit voluptatem</p>
  <div class="brand">VEXORA</div><div class="pg">23</div>
</section>

<section class="slide" style="left:462px;top:925px">
  <div class="title" style="left:9px;top:10px">MIND MAP</div>
  <svg class="abs" width="228" height="127" style="left:0;top:0" fill="none" stroke="#c4000c" stroke-width=".4">
    <polyline points="40,40 70,40 88,52"/><polyline points="50,63 75,63 84,68"/><polyline points="40,86 70,86 88,80"/>
    <polyline points="190,40 160,40 142,52"/><polyline points="178,63 153,63 144,68"/><polyline points="190,86 160,86 142,80"/>
  </svg>
  <div class="circ" style="left:86px;top:39px;width:56px;height:56px;box-shadow:0 2px 5px rgba(0,0,0,.3)" role="img" aria-label="Arena photo in a circle"></div>
  <div class="h" style="left:32px;top:35px;color:var(--red)">NEW COLOR</div><p class="p" style="left:9px;top:41px;width:44px;text-align:right">Sed ut perspiciatis unde omnis iste natus error sit voluptatem</p>
  <div class="h" style="left:42px;top:59px;color:var(--red)">NEW ENGINE</div><p class="p" style="left:20px;top:65px;width:44px;text-align:right">Sed ut perspiciatis unde omnis iste natus error sit voluptatem</p>
  <div class="h" style="left:47px;top:83px;color:var(--red)">2000CC</div><p class="p" style="left:9px;top:89px;width:44px;text-align:right">Sed ut perspiciatis unde omnis iste natus error sit voluptatem</p>
  <div class="h" style="left:178px;top:35px;color:var(--red)">DOUBLE POWER</div><p class="p" style="left:178px;top:41px;width:42px">Sed ut perspiciatis unde omnis iste natus error sit voluptatem</p>
  <div class="h" style="left:167px;top:59px;color:var(--red)">AERODYNAMIC</div><p class="p" style="left:167px;top:65px;width:44px">Sed ut perspiciatis unde omnis iste natus error sit voluptatem</p>
  <div class="h" style="left:178px;top:83px;color:var(--red)">SUSPENSION</div><p class="p" style="left:178px;top:89px;width:42px">Sed ut perspiciatis unde omnis iste natus error sit voluptatem</p>
  <div class="brand">VEXORA</div><div class="pg">24</div>
</section>

<!-- Row 9 -->
<section class="slide" style="left:2px;top:1057px">
  <div class="title" style="left:9px;top:10px">FUNNEL INFOGRAPHIC</div>
  <p class="p" style="left:30px;top:43px;width:80px">Use agile methods to give a robust summary for high level reviews. Repeated approaches to shared strategy build team thinking further for the overall value offer.</p>
  <div class="num" style="left:30px;top:69px;font-size:4px;color:var(--red)">+50K</div><p class="p" style="left:30px;top:76px">A wonderful calm has taken.</p>
  <div class="num" style="left:77px;top:69px;font-size:4px;color:var(--red)">65%</div><p class="p" style="left:77px;top:76px">A wonderful calm has taken.</p>
  <div class="num" style="left:30px;top:89px;font-size:4px;color:var(--red)">30%</div><p class="p" style="left:30px;top:96px">A wonderful calm has taken.</p>
  <div class="num" style="left:77px;top:89px;font-size:4px;color:var(--red)">+85K</div><p class="p" style="left:77px;top:96px">A wonderful calm has taken.</p>
  <svg class="abs" width="228" height="127" style="left:0;top:0">
    <polygon points="120,40 206,40 200,51 126,51" fill="#c4000c"/>
    <polygon points="129,58 197,58 191,69 135,69" fill="#aaa"/>
    <polygon points="137,76 189,76 183,87 143,87" fill="#ddd"/>
    <polygon points="145,94 181,94 175,105 151,105" fill="#999"/>
    <g font-family="Oswald,sans-serif" font-size="3.6" fill="#fff" text-anchor="middle"><text x="163" y="47">OIL</text><text x="163" y="65">ENGINE</text><text x="163" y="83">SUSPENSION</text><text x="163" y="101">MOTOR</text></g>
  </svg>
  <div class="brand">VEXORA</div><div class="pg">25</div>
</section>

<section class="slide" style="left:232px;top:1057px">
  <div class="title" style="left:9px;top:10px;text-transform:none">Management Team</div>
  <div class="abs" style="left:28px;top:39px;width:34px;height:34px;border-radius:50%;background:#ccc;border:2px solid #e6e6e6" role="img" aria-label="Team member portrait"></div>
  <div class="h" style="left:45px;top:77px;transform:translateX(-50%);font-size:4px">Marten Alvik</div>
  <div class="p" style="left:45px;top:83px;transform:translateX(-50%);color:var(--red);font-size:3px;white-space:nowrap">Project Manager</div>
  <p class="p" style="left:16px;top:89px;width:58px;text-align:center">Lorem ipsum is a standard dummy text used in layout for print, graphic or web designs.</p>
  <div class="abs" style="left:97px;top:39px;width:34px;height:34px;border-radius:50%;background:#ccc;border:2px solid #e6e6e6" role="img" aria-label="Team member portrait"></div>
  <div class="h" style="left:114px;top:77px;transform:translateX(-50%);font-size:4px">Dara Quell</div>
  <div class="p" style="left:114px;top:83px;transform:translateX(-50%);color:var(--red);font-size:3px;white-space:nowrap">Client Dept. Chief</div>
  <p class="p" style="left:85px;top:89px;width:58px;text-align:center">Lorem ipsum is a standard dummy text used in layout for print, graphic or web designs.</p>
  <div class="abs" style="left:166px;top:39px;width:34px;height:34px;border-radius:50%;background:#ccc;border:2px solid #e6e6e6" role="img" aria-label="Team member portrait"></div>
  <div class="h" style="left:183px;top:77px;transform:translateX(-50%);font-size:4px">Noa Brint</div>
  <div class="p" style="left:183px;top:83px;transform:translateX(-50%);color:var(--red);font-size:3px;white-space:nowrap">Creative Director</div>
  <p class="p" style="left:154px;top:89px;width:58px;text-align:center">Lorem ipsum is a standard dummy text used in layout for print, graphic or web designs.</p>
  <div class="brand">VEXORA</div><div class="pg">26</div>
</section>

<section class="slide" style="left:462px;top:1057px">
  <div class="photo" style="left:119px;top:0;width:94px;height:127px" role="img" aria-label="Colourful esports arena"></div>
  <svg class="abs" width="228" height="127" style="left:0;top:0"><polygon points="60,20 187,20 130,107 5,107" fill="#fff" stroke="#c4000c" stroke-width=".8"/></svg>
  <div class="title" style="left:59px;top:32px;font-size:7px">CONTACT US NOW</div>
  <p class="p" style="left:59px;top:45px;width:90px;color:#444">A wonderful calm has taken hold of my whole mind, like these sweet evenings of spring which I enjoy with my whole heart. I am alone and feel the charm of this place.</p>
  <div class="btn" style="left:59px;top:63px;font-size:2.4px;border-radius:3px;padding:1px 5px">Learn More</div>
  <div class="abs" style="left:41px;top:88px;display:flex;gap:8px;align-items:center;font-size:2.4px;color:#999">
    <span style="display:flex;align-items:center;gap:2px"><i style="width:4px;height:4px;border-radius:50%;background:var(--red)"></i>Fanpage</span>
    <span style="display:flex;align-items:center;gap:2px"><i style="width:4px;height:4px;border-radius:50%;background:var(--red)"></i>Updates</span>
    <span style="display:flex;align-items:center;gap:2px"><i style="width:4px;height:4px;border-radius:50%;background:var(--red)"></i>hello@vexora-events.com</span>
  </div>
  <div class="brand" style="left:12px">VEXORA</div>
</section>

</body>
</html>
```